Halt and Thicken New Branding Stationary Set - updated Oct 30th 2017

Updated on 30th Oct 2017 as we now need a whole folder design instead of a folder cover. We have thought out exactly what should be on it so it wont be hard. We are happy for this to be completed only by the winning designer if you like. And also we are guaranteeing this project now. Thanks!

We just got our new logo and now we would like a stationary set so we can brand our company communications. The items we need designed are:
Business cards
Letterhead
Appointment confirmation cards
Folder - switched from folder cover. Note that if you don't wish to do this unless you are selected as the winner this is fine.

1. Business cards - for 5 employees, final names will be given once the winner is selected, but you can use this one as the sample:
Lucinda Prieto
Hair Regrowth Expert
Halt and Thicken
7127 Marbury Ave, Suite 500
Kestrel Park CA 90877
lucinda@gavinthorpemd.example
(555) 238-9016

2. Letterhead 8.5" x 11.0" vertical
Halt and Thicken
Kestrel Park CA 90877
office@haltandthicken.example
(555) 238-9016

3. Appointment Confirmation cards - business card size
Halt and Thicken
Kestrel Park CA 90877
Appointment For:
Date:
Time:
If you are unable to make your appointment, please contact us to reschedule at:
(555) 238-9016
info@gavinthorpemd.example

*UPDATED*
4. Folder 9" x 12 " vertical with double pocket
We would like the infinity image from the logo made really big so the left side is on the back and the right side with the + sign is on the front and its takes up the maximum room on the folder.
On the front below the half logo it should say "A Biochemical Revolution..."
On the inside we would also like to have the infinity sign from the logo but faded and half on the left pocket half on the right.
On left inside pocket it should say (this will be partically written on top of the logo):
Gavin Thorpe MD
Precision Medicine
Halt and Thicken Hair
On the Right inside pocket it should say the following:
Because the Enemy of BETTER Health is Good Health
BETTER Ingredients
BETTER Recipe
BETTER Medicine
On the back below the logo on the bottom should be the contact information.
I attached a picture of our drawing of what we want for this to make it easier.

Here is our website to give you an idea of our branding: http://www.haltandthicken.example/

We are the only true cure for hair loss and need to look professional and highest quality and beyond reproach from an ethical standpoint. We are a medical clinic so this should be portrayed also.
We cured hair loss by analyzing biochemistry and rebalancing it so that the process reverses and your own hair can grow back naturally.

Business card information:

OK so here is the information for the business cards:

Lucinda Prieto
Hair Regrowth Expert
(555) 238-9016
www.haltandthicken.example

Marisol Quintero
Hair Growth Consultant
(555) 238-9016
marisol@gavinthorpemd.example
www.haltandthicken.example

Glenda Hutchins
CMO/COO
(555) 238-9016
glenda@haltandthicken.example
www.haltandthicken.example

Dr Lou Thorpe
President
(555) 238-9016
info@gavinthorpemd.example
www.haltandthicken.example

Halt and Thicken
Customer Service
(555) 238-9016
info@gavinthorpemd.example
www.haltandthicken.example

Target Market(s)

Men aged 20-24 who care about their appearance, care about their hair and care about the world.

Industry/Entity Type

Medical And Science

Font styles to use
Sans Serif

Colors
00a990
ffffff
9d9d9d
333333

Requirements
Must have
• Must use the logo and our brand colors from the logo in all designs.
• The pantone colors are:
• Green: #4ca26f
• Light Grey: #999999
• The design should be symmetrical and balanced.
Nice to have
• It should look reasonably masculine.
Should not have
• Do not include any red in the design.

```html
<!DOCTYPE html>
<html lang="en">
<head>
<meta charset="utf-8">
<title>Halt and Thicken – Business Card</title>
<link rel="stylesheet" href="https://fonts.googleapis.com/css2?family=Open+Sans:wght@400;600;700&display=swap">
<style>
  :root {
    --backdrop: #e6e7e8;
    --card-dark: #333436;
    --card-white: #f6f6f6;
    --brand-green: #3f9d62;
    --brand-grey: #999999;
    --band-grey: #646466;
    --text-light: #ffffff;
    --text-grey: #6e6e6e;
  }
  * { box-sizing: border-box; margin: 0; padding: 0; }
  html, body {
    width: 1200px; height: 904px; overflow: hidden;
    background: var(--backdrop);
    font-family: "Open Sans", sans-serif;
  }
  .stage {
    width: 1200px; height: 904px;
    display: flex; flex-direction: column; align-items: center; justify-content: center;
    gap: 44px;
  }
  .card {
    width: 600px; height: 343px;
    border-radius: 22px;
    overflow: hidden;
    position: relative;
    box-shadow: 0 6px 18px rgba(0,0,0,0.18);
  }
  .card--back {
    background: var(--card-dark);
    display: flex; align-items: center; justify-content: center;
  }
  .wordmark {
    display: flex; align-items: center; gap: 12px;
    font-weight: 700; text-transform: uppercase; letter-spacing: 0.5px;
  }
  .wordmark__dot { border-radius: 50%; }
  .card--back .wordmark { color: var(--brand-grey); font-size: 30px; }
  .card--back .wordmark__dot { width: 30px; height: 30px; background: var(--brand-green); }

  .card--front { background: var(--card-white); }
  .front__identity {
    position: absolute; top: 0; left: 0; right: 0; height: 205px;
    display: flex; flex-direction: column; align-items: center; justify-content: center;
    padding-top: 10px;
  }
  .card--front .wordmark { color: var(--brand-green); font-size: 28px; margin-bottom: 18px; }
  .card--front .wordmark__dot { width: 26px; height: 26px; background: var(--brand-grey); }
  .person__name { color: var(--brand-green); font-weight: 700; font-size: 21px; line-height: 1.2; }
  .person__title { color: var(--text-grey); font-size: 17px; line-height: 1.3; }

  .front__bands {
    position: absolute; left: 0; right: 0; bottom: 0; height: 138px;
    display: flex;
  }
  .band { color: var(--text-light); display: flex; flex-direction: column; justify-content: center; }
  .band--address {
    background: var(--band-grey); width: 46%;
    align-items: flex-end; text-align: right; padding-right: 22px;
    font-size: 15.5px; line-height: 1.4;
  }
  .band--address .company { font-weight: 700; }
  .band--contact {
    background: var(--brand-green); flex: 1;
    padding-left: 22px; font-size: 15px; line-height: 1.65;
  }
  .contact-line { display: flex; align-items: center; gap: 10px; }
  .contact-line svg { width: 14px; height: 14px; flex: none; }
</style>
</head>
<body>
<main class="stage">
  <section class="card card--back" aria-label="Business card back">
    <div class="wordmark"><span class="wordmark__dot"></span>Halt and Thicken</div>
  </section>

  <section class="card card--front" aria-label="Business card front">
    <div class="front__identity">
      <div class="wordmark"><span class="wordmark__dot"></span>Halt and Thicken</div>
      <div class="person__name">Lucinda Prieto</div>
      <div class="person__title">Hair Regrowth Expert</div>
    </div>
    <div class="front__bands">
      <div class="band band--address">
        <span class="company">Halt and Thicken</span>
        <span>7127 Marbury Ave, Suite 500</span>
        <span>Kestrel Park CA 90877</span>
      </div>
      <div class="band band--contact">
        <div class="contact-line">
          <svg viewBox="0 0 16 16" aria-hidden="true"><path d="M3 1.5l2.5 0 1.2 3.2-1.6 1.2c.8 1.8 2.2 3.2 4 4l1.2-1.6 3.2 1.2v2.5c0 .8-.7 1.5-1.5 1.5C6.6 13.5 1.5 8.4 1.5 3c0-.8.7-1.5 1.5-1.5z" fill="#fff"/></svg>
          <span>(555) 238-9016</span>
        </div>
        <div class="contact-line">
          <svg viewBox="0 0 16 16" aria-hidden="true"><rect x="1" y="3" width="14" height="10" rx="1.5" fill="#fff"/><path d="M1.5 4l6.5 5 6.5-5" stroke="#3f9d62" stroke-width="1.4" fill="none"/></svg>
          <span>lucinda@gavinthorpemd.example</span>
        </div>
        <div class="contact-line">
          <svg viewBox="0 0 16 16" aria-hidden="true"><circle cx="8" cy="8" r="6.5" fill="none" stroke="#fff" stroke-width="1.4"/><ellipse cx="8" cy="8" rx="2.8" ry="6.5" fill="none" stroke="#fff" stroke-width="1.2"/><path d="M1.5 8h13" stroke="#fff" stroke-width="1.2"/></svg>
          <span>www.gavinthorpemd.example</span>
        </div>
      </div>
    </div>
  </section>
</main>
</body>
</html>
```